Label design for high quality nutritional supplement brand

We need a new label design for our dietary supplement brand "NorlumPlus" from Germany. We sell high-quality nutritional supplements that help improve overall well-being.

All products in our range should receive the new label. You can find our current design on our homepage norlumplus-shop.example. The new design should be completely redesigned and look modern, fresh, high quality, minimalist and clean. We prefer the colors nude, green and earth tones.

The newly created label should contain our NorlumPlus logo. For this reason you will find this file attached. You will also find our current label, which needs to be renewed, in the appendix.

Colors

Designer to choose colors to be used in the design.

Requirements
Must have
• NorlumPlus logo

```html
<!DOCTYPE html>
<html lang="de">
<head>
<meta charset="utf-8">
<title>NorlumPlus Daily Core Protein-Shake Etiketten</title>
<link rel="stylesheet" href="https://fonts.googleapis.com/css2?family=Montserrat:wght@400;500;600&family=Vollkorn:wght@700;800&family=Yesteryear&display=swap">
<style>
  :root {
    --page-bg: #ffffff;
    --label-light: #f6f6f6;
    --label-shade: #e4e4e4;
    --ink: #1f1f1f;
    --ink-soft: #333333;
    --vanilla-band: #ead6a9;
    --vanilla-accent: #d3b574;
    --vanilla-tag: #e0c88f;
    --vanilla-art-a: #f4efdc;
    --vanilla-art-b: #4a3424;
    --choc-band: #7a5a4c;
    --choc-accent: #4a2620;
    --choc-tag: #5a3028;
    --choc-art-a: #6b3a2a;
    --choc-art-b: #3b1d14;
  }
  * { margin: 0; padding: 0; box-sizing: border-box; }
  html, body {
    width: 1200px; height: 1200px; overflow: hidden;
    background: var(--page-bg);
  }
  .canvas { position: relative; width: 1200px; height: 1200px; }

  .label {
    position: absolute; top: 235px;
    width: 540px; height: 730px;
    overflow: hidden;
    background: linear-gradient(90deg, var(--label-shade) 0%, var(--label-light) 45%, var(--label-light) 70%, var(--label-shade) 100%);
    color: var(--ink);
  }
  .label--vanilla { left: 40px; --band: var(--vanilla-band); --accent: var(--vanilla-accent); --tag: var(--vanilla-tag); --tag-ink: var(--ink-soft); }
  .label--choc { left: 620px; --band: var(--choc-band); --accent: var(--choc-accent); --tag: var(--choc-tag); --tag-ink: #f3ece8; }

  .side-band {
    position: absolute; left: 40px; top: 0; bottom: 0; width: 48px;
    background: var(--band);
    display: flex; align-items: center; justify-content: center;
  }
  .side-band__url {
    transform: rotate(-90deg);
    white-space: nowrap;
    font-family: "Montserrat", sans-serif; font-weight: 500;
    font-size: 14px; letter-spacing: 7px; text-transform: uppercase;
    color: var(--ink-soft);
  }

  .brand {
    position: absolute; left: 250px; top: 90px;
    display: flex; align-items: center; gap: 10px;
    white-space: nowrap;
    font-family: "Montserrat", sans-serif; font-weight: 500;
    font-size: 38px; color: var(--accent);
  }
  .brand__dot { width: 12px; height: 12px; border-radius: 50%; background: var(--accent); }

  .flavor {
    position: absolute; left: 128px; top: 225px;
    font-family: "Yesteryear", cursive; font-size: 52px;
    color: var(--accent);
    white-space: nowrap;
  }
  .product-name {
    position: absolute; left: 128px; top: 310px;
    white-space: nowrap;
    font-family: "Vollkorn", serif; font-weight: 800;
    font-size: 56px; line-height: 1; letter-spacing: 0;
    color: var(--ink);
  }
  .product-type {
    position: absolute; left: 130px; top: 392px;
    white-space: nowrap;
    font-family: "Montserrat", sans-serif; font-weight: 600;
    font-size: 33px; letter-spacing: 0.5px;
  }
  .category {
    position: absolute; left: 130px; top: 485px;
    white-space: nowrap;
    background: var(--tag); color: var(--tag-ink);
    font-family: "Montserrat", sans-serif; font-weight: 400;
    font-size: 22px; padding: 6px 10px;
  }
  .description {
    position: absolute; left: 130px; top: 545px;
    white-space: nowrap;
    font-family: "Montserrat", sans-serif; font-weight: 500;
    font-size: 24px; line-height: 1.45; color: var(--ink);
  }
  .net-weight {
    position: absolute; left: 130px; top: 644px;
    font-family: "Montserrat", sans-serif; font-weight: 500;
    font-size: 24px; color: var(--ink);
  }
  .flavor-art { position: absolute; }
  .label--vanilla .flavor-art { left: 395px; top: 615px; width: 115px; height: 85px; }
  .label--choc .flavor-art { left: 410px; top: 610px; width: 110px; height: 95px; }
</style>
</head>
<body>
<main class="canvas">

  <section class="label label--vanilla">
    <div class="side-band"><span class="side-band__url">www.norlumplus-shop.example</span></div>
    <div class="brand"><span class="brand__dot"></span>NorlumPlus</div>
    <div class="flavor">Vanille</div>
    <h1 class="product-name">DAILY CORE</h1>
    <p class="product-type">PROTEIN-SHAKE</p>
    <p class="category">Nahrungsergänzungsmittel</p>
    <p class="description">Whey Protein-Pulver mit<br>Flohsamenschalen</p>
    <p class="net-weight">Net.Wt.630g</p>
    <svg class="flavor-art" role="img" aria-label="Vanilleblüte mit Vanilleschoten" viewBox="0 0 115 85">
      <defs>
        <linearGradient id="vanillaFill" x1="0" y1="0" x2="1" y2="1">
          <stop offset="0" stop-color="var(--vanilla-art-a)"/>
          <stop offset="1" stop-color="var(--vanilla-art-b)"/>
        </linearGradient>
      </defs>
      <rect x="0" y="0" width="115" height="85" rx="14" fill="url(#vanillaFill)" opacity="0.55"/>
    </svg>
  </section>

  <section class="label label--choc">
    <div class="side-band"><span class="side-band__url">www.norlumplus-shop.example</span></div>
    <div class="brand"><span class="brand__dot"></span>NorlumPlus</div>
    <div class="flavor">Schocolade</div>
    <h1 class="product-name">DAILY CORE</h1>
    <p class="product-type">PROTEIN-SHAKE</p>
    <p class="category">Nahrungsergänzungsmittel</p>
    <p class="description">Whey Protein-Pulver mit<br>Flohsamenschalen</p>
    <p class="net-weight">Net.Wt.630g</p>
    <svg class="flavor-art" role="img" aria-label="Schokoladenstücke" viewBox="0 0 110 95">
      <defs>
        <linearGradient id="chocFill" x1="0" y1="0" x2="1" y2="1">
          <stop offset="0" stop-color="var(--choc-art-a)"/>
          <stop offset="1" stop-color="var(--choc-art-b)"/>
        </linearGradient>
      </defs>
      <rect x="0" y="0" width="110" height="95" rx="12" fill="url(#chocFill)"/>
    </svg>
  </section>

</main>
</body>
</html>
```